Stationary / namecards for a dental clinic
+ appointment cards
Modern
Dr. Leon T. Whitby
47 Corvane Street Griffith, NSW 2680 Australia
reception@corvanedentalcare.example.au
www.corvanedentalcare.example.au
Doctors names: Dr. Leon T. Whitby, BDS Dr. Samir Belkacem, DDS Dr. Martin Oosterholt, BDS Nora Pike, Dental Hygienist
appointment card

```html
<!DOCTYPE html>
<html lang="en">
<head>
<meta charset="utf-8">
<title>Corvane Dental Care – Business Card</title>
<link href="https://fonts.googleapis.com/css2?family=Open+Sans:ital,wght@0,400;0,600;1,400;1,600&display=swap" rel="stylesheet">
<style>
  :root {
    --page-bg: #eceff1;
    --card-white: #ffffff;
    --brand-blue: #1e9bd7;
    --band-blue: #28a3df;
    --brand-green: #5cae2e;
    --text-white: #ffffff;
  }
  html, body {
    margin: 0;
    padding: 0;
    width: 1200px;
    height: 914px;
    overflow: hidden;
    background: var(--page-bg);
    font-family: "Open Sans", Arial, sans-serif;
  }
  .card {
    position: absolute;
    left: 100px;
    top: 171px;
    width: 1000px;
    height: 571px;
    background: var(--card-white);
    box-shadow: 0 6px 24px rgba(0,0,0,0.18);
    overflow: hidden;
  }
  .card-backdrop {
    position: absolute;
    inset: 0;
  }
  .brand {
    position: absolute;
    left: 540px;
    top: 120px;
    display: flex;
    align-items: center;
    gap: 18px;
  }
  .brand-dot {
    width: 46px;
    height: 46px;
    border-radius: 50%;
    background: var(--brand-blue);
  }
  .brand-name {
    font-size: 62px;
    font-weight: 400;
    color: var(--brand-blue);
    line-height: 0.9;
    letter-spacing: -1px;
  }
  .holder {
    position: absolute;
    right: 540px;
    top: 372px;
    text-align: right;
    color: var(--text-white);
    font-style: italic;
  }
  .holder-name {
    font-size: 20px;
    font-weight: 600;
    margin: 0 0 16px;
  }
  .holder-address {
    font-size: 17px;
    line-height: 1.45;
    margin: 0;
  }
  .divider {
    position: absolute;
    left: 485px;
    top: 368px;
    width: 2px;
    height: 150px;
    background: var(--text-white);
  }
  .contacts {
    position: absolute;
    left: 505px;
    top: 368px;
    margin: 0;
    padding: 0;
    list-style: none;
    color: var(--text-white);
    font-size: 17px;
    font-style: italic;
  }
  .contacts li {
    display: flex;
    align-items: center;
    gap: 10px;
    height: 37px;
  }
  .contacts svg {
    width: 22px;
    height: 22px;
    flex: none;
  }
</style>
</head>
<body>
  <div class="card">
    <svg class="card-backdrop" viewBox="0 0 1000 571" preserveAspectRatio="none" aria-hidden="true">
      <path d="M0,318 C320,325 700,300 1000,205 L1000,571 L0,571 Z" fill="var(--brand-green)"/>
      <path d="M0,338 C320,345 700,322 1000,232 L1000,571 L0,571 Z" fill="var(--band-blue)"/>
    </svg>

    <div class="brand">
      <span class="brand-dot"></span>
      <span class="brand-name">corvane<br>dental care</span>
    </div>

    <div class="holder">
      <p class="holder-name">Dr. Leon T. Whitby</p>
      <p class="holder-address">47 Corvane Street Tallowmere, KVR<br>9021 Australia</p>
    </div>

    <div class="divider"></div>

    <ul class="contacts">
      <li>
        <svg viewBox="0 0 24 24"><circle cx="12" cy="12" r="11" fill="#fff"/><path d="M8.5 6.5l2 2-1.2 1.5c.8 1.7 2 2.9 3.7 3.7l1.5-1.2 2 2-1.3 1.8c-4-.8-7.4-4.2-8.2-8.2z" fill="var(--band-blue)"/></svg>
        <span>026-555-014-8</span>
      </li>
      <li>
        <svg viewBox="0 0 24 24"><circle cx="12" cy="12" r="11" fill="#fff"/><rect x="8.5" y="5.5" width="7" height="13" rx="1.2" fill="var(--band-blue)"/><rect x="9.7" y="7" width="4.6" height="8.5" fill="#fff"/></svg>
        <span>026-555-019-2</span>
      </li>
      <li>
        <svg viewBox="0 0 24 24"><circle cx="12" cy="12" r="11" fill="#fff"/><rect x="6" y="8" width="12" height="8.5" rx="1" fill="var(--band-blue)"/><path d="M6.5 8.5l5.5 4.2 5.5-4.2" stroke="#fff" stroke-width="1.2" fill="none"/></svg>
        <span>reception@corvanedentalcare.example.au</span>
      </li>
      <li>
        <svg viewBox="0 0 24 24"><circle cx="12" cy="12" r="11" fill="#fff"/><circle cx="12" cy="12" r="6.5" fill="none" stroke="var(--band-blue)" stroke-width="1.4"/><path d="M5.5 12h13M12 5.5c-2.5 3.5-2.5 9.5 0 13M12 5.5c2.5 3.5 2.5 9.5 0 13" stroke="var(--band-blue)" stroke-width="1.2" fill="none"/></svg>
        <span>www.corvanedentalcare.example.au</span>
      </li>
    </ul>
  </div>
</body>
</html>
```